DELCOUR ROOFING YARD SIGN

We need a yard sign to put in our customers' yards when we are roofing their home.
Delcour Roofing
438 Fenwick Rd
Lake Charles LA 70615
phone: 337-555-0142

Maybe some verbiage like "Your Hometown Roofing Experts"
or
"Family Owned Since 1956"

```html
<!DOCTYPE html>
<html lang="en">
<head>
<meta charset="UTF-8">
<title>Delcour Roofing Yard Sign</title>
<link href="https://fonts.googleapis.com/css2?family=Montserrat:wght@700;800;900&display=swap" rel="stylesheet">
<style>
  :root {
    --backdrop: #e6ebef;
    --sign-black: #121212;
    --silver-light: #d4d4d4;
    --silver-mid: #a9a9a9;
    --silver-dark: #8c8c8c;
    --ink: #151515;
    --paper: #f1f1f1;
  }
  * { box-sizing: border-box; margin: 0; padding: 0; }
  html, body {
    width: 1200px;
    height: 1200px;
    overflow: hidden;
    background: var(--backdrop);
    font-family: "Montserrat", sans-serif;
  }
  .canvas {
    width: 1200px;
    height: 1200px;
    display: flex;
    align-items: center;
    justify-content: center;
  }
  .yard-sign {
    width: 1000px;
    height: 860px;
    padding: 9px;
    background: linear-gradient(135deg, var(--silver-light), var(--silver-dark));
    box-shadow: 0 10px 30px rgba(0,0,0,0.18);
  }
  .sign-face {
    width: 100%;
    height: 100%;
    display: flex;
    flex-direction: column;
    background: var(--sign-black);
  }
  .brand-area {
    height: 390px;
    display: flex;
    align-items: center;
    justify-content: center;
    gap: 22px;
  }
  .brand-dot {
    width: 64px;
    height: 64px;
    border-radius: 50%;
    background: var(--paper);
  }
  .brand-name {
    color: var(--paper);
    font-weight: 800;
    font-size: 58px;
    letter-spacing: 2px;
  }
  .tagline-band {
    height: 250px;
    background: linear-gradient(100deg, var(--silver-mid) 0%, var(--silver-light) 45%, var(--silver-mid) 100%);
    display: flex;
    flex-direction: column;
    align-items: center;
    justify-content: center;
    color: var(--ink);
  }
  .headline {
    font-weight: 900;
    font-size: 74px;
    line-height: 0.98;
    text-align: center;
    letter-spacing: 1px;
  }
  .since-line {
    margin-top: 16px;
    display: flex;
    align-items: center;
    gap: 18px;
    font-weight: 800;
    font-size: 30px;
    letter-spacing: 3px;
  }
  .since-line .rule {
    width: 90px;
    height: 3px;
    background: var(--ink);
  }
  .contact-area {
    flex: 1;
    display: flex;
    flex-direction: column;
    align-items: center;
    justify-content: center;
    color: var(--paper);
  }
  .phone-row {
    display: flex;
    align-items: center;
    gap: 18px;
  }
  .phone-icon { width: 78px; height: 78px; }
  .phone-number {
    font-weight: 900;
    font-size: 92px;
    letter-spacing: 2px;
    line-height: 1;
  }
  .address {
    margin-top: 16px;
    font-weight: 800;
    font-size: 28px;
    letter-spacing: 2.5px;
  }
</style>
</head>
<body>
<main class="canvas">
  <section class="yard-sign">
    <div class="sign-face">
      <header class="brand-area">
        <span class="brand-dot"></span>
        <span class="brand-name">Delcour Roofing</span>
      </header>
      <div class="tagline-band">
        <h1 class="headline">YOUR HOMETOWN<br>ROOFING EXPERTS</h1>
        <p class="since-line"><span class="rule"></span>FAMILY OWNED SINCE 1956<span class="rule"></span></p>
      </div>
      <footer class="contact-area">
        <div class="phone-row">
          <svg class="phone-icon" viewBox="0 0 80 80" aria-hidden="true">
            <circle cx="40" cy="40" r="38" fill="#f1f1f1"/>
            <path d="M27 20c2-1 4-1 5 1l4 8c1 2 0 4-1 5l-3 2c2 5 6 9 11 11l2-3c1-1 3-2 5-1l8 4c2 1 2 3 1 5l-2 4c-1 2-3 3-6 3-15-1-28-14-29-29 0-3 1-5 3-6z" fill="#121212"/>
          </svg>
          <span class="phone-number">337-555-0142</span>
        </div>
        <p class="address">438 FENWICK RD LAKE CHARLES LA 70615</p>
      </footer>
    </div>
  </section>
</main>
</body>
</html>
```